Cover Design Brief – Prayer Book (Modern Revision)

Design a new, modern, high-quality book cover that reflects the essence of the original version. The updated cover should feel contemporary yet familiar, appealing to both younger and older readers, while evoking a sense of spiritual depth, calm, and authenticity.

1. Visual Reference to the Original Cover
Continuity:
Retain visual elements such as the color palette, central motifs (eg, geometric patterns, Islamic ornaments, or a symbolic figure), and overall structure from the original cover.

Recognition:
Readers familiar with the old cover should instantly recognize the book but be pleasantly surprised by the refined, modern look.

2. Style & Mood
Modern Islamic design, minimalist and clean rather than ornate.

Spiritual, calming, elegant – avoid overly bright or flashy visuals.

Subtle use of Islamic motifs, possibly a decorative Arabic calligraphy word like ṣalāh (صلاة) to enrich the theme.

3. Suggested Color Palette
Deep blue, teal, petrol green, olive, sand tones, or midnight blue with accents of gold – depending on the original cover scheme.

Avoid neon or loud colors.

If gold or silver is used, it should be subtle and classy (eg, foil stamping or embossing, not digital effects).

4. Typography
A modern serif font for the main title is welcome, but it should be clean and elegant.

Subtitles should use a clear, legible font.

If the title includes Arabic text, it should be displayed in tasteful classical calligraphy or a stylized script.

5. Back Cover
Will include a brief description text (to be provided later).

Clean layout, optionally with a small publisher logo.

Possibly a short quote or ḥadīth in Arabic (with or without translation) to complement the design.

6. Target Audience
German-speaking Muslims, male and female, ages 15+

Suitable for both beginners and advanced practitioners of the prayer

Designed as a long-term spiritual companion and a thoughtful gift

```html
<!DOCTYPE html>
<html lang="de">
<head>
<meta charset="utf-8">
<title>As-Ṣalāh – Das Gebet im Islam</title>
<link rel="stylesheet" href="https://fonts.googleapis.com/css2?family=Quicksand:wght@300;400;500&display=swap">
<style>
  :root {
    --night: #0d1116;
    --stone: #1c2024;
    --sky-top: #1d3550;
    --sky-mid: #3f6a86;
    --horizon: #e79a5a;
    --glow: #f6c98a;
    --rug: #7a1f1c;
    --ink: #ffffff;
  }
  html, body {
    margin: 0;
    padding: 0;
    width: 848px;
    height: 1200px;
    overflow: hidden;
    background: var(--night);
  }
  .cover {
    position: relative;
    width: 848px;
    height: 1200px;
    overflow: hidden;
    font-family: "Quicksand", sans-serif;
    color: var(--ink);
  }
  .cover-scene {
    position: absolute;
    inset: 0;
    background:
      radial-gradient(ellipse 180px 120px at 424px 930px, rgba(246,201,138,0.9), rgba(246,201,138,0) 100%),
      linear-gradient(to bottom, transparent 0, transparent 1000px, var(--rug) 1060px, #3a1010 1200px),
      linear-gradient(to right, var(--night) 0, var(--stone) 200px, transparent 232px, transparent 612px, var(--stone) 640px, var(--night) 848px),
      linear-gradient(to bottom, #0f1e30 0, var(--sky-top) 250px, var(--sky-mid) 620px, var(--horizon) 880px, var(--glow) 940px, #4a3a32 1000px);
  }
  .title-frame {
    position: absolute;
    left: 27px;
    top: 26px;
    width: 794px;
    height: 300px;
  }
  .title-seal {
    position: absolute;
    left: 360px;
    top: 43px;
    width: 128px;
    height: 128px;
    border-radius: 50%;
    border: 2px solid var(--ink);
    box-sizing: border-box;
    background: rgba(13,17,22,0.55);
  }
  .title {
    position: absolute;
    left: 0;
    right: 0;
    top: 196px;
    margin: 0;
    text-align: center;
    font-weight: 300;
    font-size: 106px;
    line-height: 1;
    letter-spacing: 1px;
  }
  .subtitle {
    position: absolute;
    left: 514px;
    top: 778px;
    margin: 0;
    font-weight: 400;
    font-size: 28px;
    letter-spacing: 0.3px;
  }
  .edition {
    position: absolute;
    left: 30px;
    top: 1108px;
    margin: 0;
    font-weight: 400;
    font-size: 15px;
    line-height: 20px;
  }
  .publisher {
    position: absolute;
    right: 30px;
    top: 1090px;
    display: flex;
    flex-direction: column;
    align-items: center;
    gap: 10px;
  }
  .publisher-mark {
    width: 40px;
    height: 40px;
    border: 2px solid var(--ink);
    border-radius: 50%;
    box-sizing: border-box;
  }
  .publisher-name {
    font-weight: 400;
    font-size: 15px;
  }
</style>
</head>
<body>
<main class="cover">
  <div class="cover-scene" role="img" aria-label="Foto: Betender Mann in einem steinernen Torbogen vor Sternenhimmel und Sonnenuntergang, auf rotem Gebetsteppich"></div>

  <svg class="title-frame" viewBox="0 0 794 300" aria-hidden="true">
    <path d="M22 0 H772 A22 22 0 0 0 794 22 V278 A22 22 0 0 0 772 300 H22 A22 22 0 0 0 0 278 V22 A22 22 0 0 0 22 0 Z"
          fill="none" stroke="#ffffff" stroke-width="1"/>
  </svg>

  <div class="title-seal" role="img" aria-label="Arabische Kalligrafie des Wortes Ṣalāh im Kreis"></div>

  <h1 class="title">As-Ṣalāh</h1>
  <p class="subtitle">Das Gebet im Islam</p>

  <p class="edition">Vollständig<br>revidierte<br>Ausgabe</p>

  <div class="publisher">
    <span class="publisher-mark"></span>
    <span class="publisher-name">Lichtpfad Verlag</span>
  </div>
</main>
</body>
</html>
```